Logo & Business card - Want to paint the town?

Brushvane - Top Quality Painting & Decorating

Brushvane are a painting & decorating company who work predominantly in the residential market and not commercial. We require a logo and business cards design

The company is based Christchurch NZ. Christchurch had major earthquakes in 2010 and 2011, which devastated the city. The city is in rebuild and fixing phase and will be for the next 5 years to get the city back on it's feet. As a result of the earthquakes are a lot of homes being fixed that require painting and decorating.

Additional to the earthquake work there is also huge growth in the city meaning lots of new homes are being built to accommodate the growth.

Alongside this there is an every growing rental market, so we not only work on residential earthquake repairs and new builds but also work with real estate agents, property managers and interior designers.

Christchurch has seen a large number of tradesmen enter the market and not all of whom are qualified/skilled. Our company’s painters are those with years of experience and who pride themselves on top quality precision work.

Brushvane are about quality jobs, done to a very high level at an affordable price. We are not the cheapest but also not the most expensive. Our logo and cards must reflect the quality of our work. Brushvane requires a professional logo and business card targeted to the higher end of the residential market.

Target Market(s)

Builders requiring contract painters, housing companies such as Tom Halvey, Kestrel buildings, Harbor Nest etc., real estate agents, property managers, interior designers and home owners.

The business cards and logo must appeal to builders, homeowner, interior designers and real estate agents so can’t be too masculine/feminine.

It needs to be bold, professional and stylish.

Industry/Entity Type

Residential

Logo Text

Brushvane

Logo styles of interest
Wordmark Logo
Requirements
Must have
• The logo and business cards must be bold, clean, modern, smart, simple, self explanatory, tidy, easy to read, timeless, and not frilly.

We are about quality, precision and being able to cut a straight line, so the card needs to avoid and curvy brush strokes as this denotes a bad a and sloppy painter.

The card and logo must scream top quality and affordability.
The card must be clean and modern, high end and stylish.

The logo must be something, which will go well on a silver/ black background as eventually as the van fleet will be either silver or black, so it must punch out on these colours.

For contact details that need to appear on the business cards see the full brief attached.
Nice to have
• One idea could be to have a picture on the business card of a well-painted stylish modern home interior, which would eventually be replaced by picture of Brushvane's paint jobs.
Should not have
• It definitely must not include is paint drips; paint pot with dribbles over the side of it, splurges of paint, or paintbrush swooshes as this indicates a messy painter.

Most colours are ok except for pink, orange or pastel colours.

```html
<!DOCTYPE html>
<html lang="en">
<head>
<meta charset="utf-8">
<title>Brushvane Business Card</title>
<link rel="stylesheet" href="https://fonts.googleapis.com/css2?family=Cinzel:wght@400&family=Lato:wght@400&family=Open+Sans:wght@600&family=PT+Sans+Narrow:wght@700&family=Noto+Sans+Mono:wght@700&family=Noto+Serif:wght@400&display=swap">
<style>
  :root {
    --page: #ffffff;
    --card: #aeaa79;
    --card-edge: #2b2a22;
    --ink: #111111;
    --house-tone: rgba(140, 142, 115, 0.45);
  }
  * { margin: 0; padding: 0; box-sizing: border-box; }
  html, body {
    width: 927px; height: 1200px; overflow: hidden;
    background: var(--page);
  }
  .canvas { position: relative; width: 927px; height: 1200px; }
  .card {
    position: absolute; left: 12px; top: 274px;
    width: 903px; height: 406px;
    background: var(--card);
    border: 1.5px solid var(--card-edge);
    overflow: hidden;
    color: var(--ink);
  }
  .house-art {
    position: absolute; left: 300px; top: 140px; width: 300px; height: 190px;
    background: linear-gradient(180deg, rgba(140,142,115,0) 0%, var(--house-tone) 45%, rgba(140,142,115,0.2) 100%);
  }
  .wordmark {
    position: absolute; left: 0; right: 0; top: 0;
    text-align: center;
    font-family: "Cinzel", serif; font-weight: 400;
    font-size: 72px; letter-spacing: 2px; line-height: 1;
  }
  .tagline {
    position: absolute; left: 0; right: 0; top: 76px;
    text-align: center;
    font-family: "Lato", sans-serif;
    font-size: 37px; font-variant: small-caps; line-height: 1;
    white-space: nowrap;
  }
  .tagline .cap { font-size: 52px; }
  .contact { position: absolute; }
  .contact--left { left: 12px; top: 187px; }
  .contact--right { left: 543px; top: 170px; }
  .contact__name { line-height: 1; white-space: nowrap; }
  .contact--left .contact__name {
    font-family: "Open Sans", sans-serif; font-weight: 600; font-size: 36px;
  }
  .contact--right .contact__name {
    font-family: "PT Sans Narrow", sans-serif; font-weight: 700; font-size: 43px;
  }
  .contact__line {
    font-family: "Noto Sans Mono", monospace; font-weight: 700; font-size: 24px;
    white-space: nowrap; line-height: 1;
  }
  .contact__label {
    font-family: "Noto Serif", serif; font-weight: 400; font-size: 30px;
  }
  .contact--left .phone { margin-top: 16px; }
  .contact--left .email { margin-top: 28px; }
  .contact--left .web { margin-top: 38px; }
  .contact--right .phone { margin-top: 24px; }
  .contact--right .email { margin-top: 28px; }
  .contact--right .web { margin-top: 23px; }
</style>
</head>
<body>
<main class="canvas">
  <section class="card">
    <div class="house-art" role="img" aria-label="Faint illustration of a house"></div>

    <h1 class="wordmark">Brushvane</h1>
    <p class="tagline"><span class="cap">T</span>op <span class="cap">Q</span>uality <span class="cap">P</span>ainting &amp; <span class="cap">D</span>ecorating</p>

    <div class="contact contact--left">
      <p class="contact__name">Marco Del Vale</p>
      <p class="contact__line phone"><span class="contact__label">T:</span>022 555 01 10</p>
      <p class="contact__line email"><span class="contact__label">E:</span>info@brushvane.co.zn</p>
      <p class="contact__line web">www.brushvane.co.zn</p>
    </div>

    <div class="contact contact--right">
      <p class="contact__name">Jenna Corliss</p>
      <p class="contact__line phone"><span class="contact__label">T:</span>021 555 06 98</p>
      <p class="contact__line email"><span class="contact__label">E:</span>info@brushvane.co.zn</p>
      <p class="contact__line web">www.brushvane.co.zn</p>
    </div>
  </section>
</main>
</body>
</html>
```